Stationery - Jewellers
Business Card, Letterhead, Envelope.
I need double sided standard sized Business Card [3.5" x 2"]
Anything that looks good. Including the fonts in logo.
Professional
Imran Kazemi
Proprietor
148 Wexcombe Lane
BX4 7QT
Leeds
United Kingdom
info@corwinthegoldcrafts.co.uk
corwinthegoldcrafts.co.uk
I will welcome any ideas.
Logo and tagline: Professionals in making your loved ones smile..
Website address.
Find us on Facebook/Twitter logos.

```html
<!DOCTYPE html>
<html lang="en">
<head>
<meta charset="utf-8">
<title>Corwin The Goldcrafts – Business Card</title>
<link rel="stylesheet" href="https://fonts.googleapis.com/css2?family=Tinos:wght@400;700&family=Arimo:wght@400&display=swap">
<style>
  :root {
    --backdrop: #4a2417;
    --gold-light: #fbe98a;
    --gold-mid: #eac84a;
    --gold-deep: #c69229;
    --band: #0c0b09;
    --ink: #141210;
    --logo-gold: #e2bd55;
    --seal-gold: #d9b04a;
  }
  * { margin: 0; padding: 0; box-sizing: border-box; }
  html, body {
    width: 1200px;
    height: 935px;
    overflow: hidden;
    background: var(--backdrop);
  }
  .business-card {
    position: absolute;
    left: 100px;
    top: 182px;
    width: 1000px;
    height: 571px;
    border-radius: 42px;
    overflow: hidden;
    background:
      linear-gradient(115deg, rgba(255,255,255,0) 20%, rgba(255,250,210,0.45) 38%, rgba(255,255,255,0) 55%),
      linear-gradient(160deg, var(--gold-light) 0%, var(--gold-mid) 40%, var(--gold-deep) 100%);
    box-shadow: 0 14px 34px rgba(0,0,0,0.45);
  }
  .holder {
    position: absolute;
    right: 64px;
    top: 44px;
    text-align: right;
    font-family: "Tinos", "Times New Roman", serif;
    font-weight: 700;
    color: var(--ink);
    text-transform: uppercase;
  }
  .holder-name { font-size: 30px; letter-spacing: 0.5px; line-height: 1.1; }
  .holder-role { font-size: 18px; margin-top: 6px; }
  .logo-band {
    position: absolute;
    left: 0;
    top: 170px;
    width: 100%;
    height: 210px;
    background: var(--band);
  }
  .brand-name {
    position: absolute;
    left: 160px;
    top: 50%;
    transform: translateY(-50%);
    font-family: "Tinos", "Times New Roman", serif;
    font-weight: 400;
    font-size: 40px;
    color: var(--logo-gold);
    white-space: nowrap;
  }
  .brand-mark {
    position: absolute;
    left: 584px;
    top: 164px;
    width: 222px;
    height: 222px;
  }
  .address {
    position: absolute;
    right: 535px;
    top: 440px;
    text-align: right;
    font-family: "Arimo", Arial, sans-serif;
    font-style: normal;
    font-size: 22px;
    line-height: 1.4;
    color: var(--ink);
  }
  .contact {
    position: absolute;
    left: 500px;
    top: 426px;
    font-family: "Arimo", Arial, sans-serif;
    font-size: 21px;
    line-height: 1.45;
    color: var(--ink);
    white-space: nowrap;
  }
  .contact .label { display: inline-block; width: 66px; }
</style>
</head>
<body>
  <section class="business-card">
    <div class="holder">
      <div class="holder-name">Imran Kazemi</div>
      <div class="holder-role">Proprietor</div>
    </div>

    <div class="logo-band">
      <div class="brand-name">Corwin The Goldcrafts</div>
    </div>

    <svg class="brand-mark" viewBox="0 0 200 200" aria-hidden="true">
      <circle cx="100" cy="100" r="98" fill="var(--seal-gold)"/>
    </svg>

    <address class="address">
      148 Wexcombe Lane&nbsp; BX4 7QT Leeds<br>
      United Kingdom
    </address>

    <div class="contact">
      <div><span class="label">Phone</span>: 0113 496 0732</div>
      <div><span class="label">Fax</span>: 0113 496 0418</div>
      <div><span class="label">Email</span>: info@corwinthegoldcrafts.co.uk</div>
    </div>
  </section>
</body>
</html>
```